Verantix - Solution provider in business consulting

Verantix is a swiss based company providing solutions for developing markets. The business covers various fields of business consulting, such as supply chain, product costs, quality management and manufacturing management. The Business operates in a efficient, straight and solution oriented manner.
The final design should communicate these characteristics. Asian people as well as as western people shall identify the qualities of the company at first sight.
The customer needs business cards with a simple view but an recognizable design, printed in high quality. Engraved elements such as the globe or simple words are possible.
Available colors are: (RAL)
102/102/102
51/102/102
153/204/153
255/102/51
Font: Calibri
Industry/Entity Type
Business
Look and feel
Each slider illustrates characteristics of the customer's brand and the style your logo design should communicate.

```html
<!DOCTYPE html>
<html lang="en">
<head>
<meta charset="utf-8">
<title>Verantix – Business Cards</title>
<link rel="stylesheet" href="https://fonts.googleapis.com/css2?family=Carlito:wght@400;700&display=swap">
<style>
  :root {
    --stage: #000000;
    --card-light: #f2f2f2;
    --card-dark: #666666;
    --ink: #5a5a5a;
    --ink-soft: #666666;
    --ink-light: #ffffff;
    --radius: 46px;
  }
  * { margin: 0; padding: 0; box-sizing: border-box; }
  html, body {
    width: 1200px;
    height: 900px;
    overflow: hidden;
    background: var(--stage);
    font-family: "Carlito", Calibri, sans-serif;
  }
  .stage { position: relative; width: 1200px; height: 900px; }

  .card { position: absolute; top: 200px; width: 310px; height: 502px; }

  .card--front {
    left: 265px;
    background: var(--card-light);
    border-radius: var(--radius) 0 var(--radius) 0;
    color: var(--ink);
  }
  .card--back {
    left: 641px;
    width: 309px;
    background: var(--card-dark);
    border-radius: 0 var(--radius) 0 var(--radius);
  }

  .wordmark {
    position: absolute;
    font-weight: 400;
    letter-spacing: 0.5px;
    line-height: 1;
  }
  .card--front .wordmark {
    left: 29px; top: 64px;
    font-size: 48px;
    color: var(--ink-soft);
  }
  .card--back .wordmark {
    left: 27px; top: 388px;
    font-size: 66px;
    color: var(--ink-light);
  }

  .person { position: absolute; left: 29px; top: 285px; }
  .person__name { font-size: 18px; font-weight: 700; line-height: 22px; }
  .person__role { font-size: 14px; line-height: 18px; }

  .address {
    position: absolute; left: 29px; top: 341px;
    font-size: 14px; line-height: 18px; font-style: normal;
  }

  .contacts {
    position: absolute; left: 28px; top: 396px;
    list-style: none; font-size: 14px;
  }
  .contacts li { display: flex; align-items: center; height: 20.7px; }
  .contacts svg { width: 11px; height: 11px; margin-right: 9px; fill: var(--ink); }
</style>
</head>
<body>
<main class="stage">

  <section class="card card--front" aria-label="Business card front">
    <div class="wordmark">verantix</div>

    <div class="person">
      <div class="person__name">Marco Lenz</div>
      <div class="person__role">CEO</div>
    </div>

    <address class="address">
      Verantix GmbH Feldweg 14<br>
      8570 Weinfelden Switzerland
    </address>

    <ul class="contacts">
      <li>
        <svg viewBox="0 0 12 12" aria-hidden="true"><path d="M3.5 0.5h5a1 1 0 0 1 1 1v9a1 1 0 0 1-1 1h-5a1 1 0 0 1-1-1v-9a1 1 0 0 1 1-1zM3.8 1.8v7.4h4.4V1.8z"/></svg>
        +41 79 000 1234
      </li>
      <li>
        <svg viewBox="0 0 12 12" aria-hidden="true"><path d="M2.4 0.8l1.9 2.3-1 1.2c.7 1.6 2 2.9 3.5 3.6l1.2-1 2.3 1.9-1.2 1.9C5 10.5 1.5 7 .6 2z"/></svg>
        +41 71 000 5678
      </li>
      <li>
        <svg viewBox="0 0 12 12" aria-hidden="true"><path d="M0.5 2.5h11v7h-11zM1.5 3.3v.6L6 6.6l4.5-2.7v-.6z"/></svg>
        marco.lenz@verantix.ch
      </li>
      <li>
        <svg viewBox="0 0 12 12" aria-hidden="true"><circle cx="6" cy="6" r="5.5"/></svg>
        www.verantix.ch
      </li>
    </ul>
  </section>

  <section class="card card--back" aria-label="Business card back">
    <div class="wordmark">verantix</div>
  </section>

</main>
</body>
</html>
```